Stationary, Envelope, Folder, Brochure
brightmendhome.example
Stationary, Envelope, Folder, Brochure - Health
Creative Brief
Health
Corporate, and Patients. Something bright and uplifting to grab the brightmend home feeling when people look at our materials. I like the QVR Petal Courier Lad logo and some of the materials they use. It has an uplifting look and feel.
Provide the materials listed in the Title. Use the uploaded picture logo.
quietharborwatch quietharborwatch
Colors: I do like the Blues and the gradient from a darker to a brighter blue. Maybe even do that more with other bright colors. Have fun explore a little and think outside the box. Will try to provide with as much feedback as possible. -Desmond
Hi Everyone, Keep in mind we want a look and feel of "BRIGHT Mend Home" and putting the "Care" back into healthcare. Having a bright and professional look that will excite the senses when a person looks at the material. We do not want to be the "norm" of home health. Our clients are of all ages for example 20+. Lets get excited, creative, and see what we can come up with. Also "Brightmend Home" Font needs to also be fun and represent the logo and spirit of the great experience our company provide unlike others.

```html
<!DOCTYPE html>
<html lang="en">
<head>
<meta charset="utf-8">
<title>Brightmend Home — Stationery Set</title>
<link href="https://fonts.googleapis.com/css2?family=Open+Sans:wght@400;600&display=swap" rel="stylesheet">
<style>
  :root {
    --navy: #0a2740;
    --deep-blue: #0f4d7a;
    --bright-blue: #1e8fd0;
    --sky: #5fc0f0;
    --brand-blue: #1f6fb0;
    --paper: #ffffff;
    --stage: #f4f5f6;
    --frame: #c9cbce;
    --ink: #5a6068;
    --shadow: rgba(0, 0, 0, 0.22);
  }
  html, body {
    margin: 0;
    padding: 0;
    overflow: hidden;
  }
  body {
    width: 1200px;
    height: 772px;
    background: var(--paper);
    font-family: "Open Sans", Arial, sans-serif;
    position: relative;
  }
  .stage {
    position: absolute;
    left: 12px; top: 12px;
    width: 1174px; height: 746px;
    border: 2px solid var(--frame);
    background: var(--stage);
  }
  .sheet {
    position: absolute;
    background: var(--paper);
    box-shadow: 3px 4px 10px var(--shadow);
    overflow: hidden;
  }
  .band { position: absolute; left: 0; top: 0; width: 100%; display: block; }

  /* Letterhead */
  .letterhead { left: 192px; top: 96px; width: 420px; height: 588px; }
  .brand {
    position: absolute;
    display: flex;
    align-items: center;
    gap: 6px;
    color: var(--brand-blue);
    font-weight: 400;
    white-space: nowrap;
  }
  .brand .dot {
    border-radius: 50%;
    background: var(--bright-blue);
    flex: none;
  }
  .letterhead .brand { left: 16px; top: 62px; font-size: 15px; }
  .letterhead .brand .dot { width: 16px; height: 16px; }
  .tagline {
    position: absolute;
    left: 38px; top: 82px;
    font-size: 6px;
    color: var(--ink);
    letter-spacing: 0.5px;
    white-space: nowrap;
  }
  .watermark {
    position: absolute;
    left: 40px; top: 230px;
    width: 340px;
    text-align: center;
    font-size: 20px;
    color: var(--brand-blue);
    opacity: 0.12;
    white-space: nowrap;
  }
  .footer-block {
    position: absolute;
    font-size: 5.5px;
    line-height: 8px;
    color: var(--ink);
    white-space: nowrap;
  }
  .footer-contact { left: 42px; top: 486px; }
  .footer-address { left: 290px; top: 490px; text-align: left; }

  /* Business card */
  .card { left: 70px; top: 302px; width: 116px; height: 68px; }
  .card-panel { position: absolute; left: 0; top: 0; height: 100%; width: 46px; display: block; }
  .card .brand { left: 45px; top: 29px; font-size: 5px; gap: 3px; }
  .card .brand .dot { width: 5px; height: 5px; }

  /* Envelope front */
  .envelope-front { left: 684px; top: 108px; width: 444px; height: 204px; }

  /* Envelope back */
  .envelope-back { left: 684px; top: 384px; width: 444px; height: 228px; }
  .flap { position: absolute; left: 0; top: 0; width: 100%; display: block; }
  .envelope-back .brand {
    left: 0; width: 100%;
    top: 34px;
    justify-content: center;
    color: var(--sky);
    font-size: 9px;
    gap: 4px;
  }
  .envelope-back .brand .dot { width: 10px; height: 10px; background: var(--sky); }
</style>
</head>
<body>
<main class="stage">

  <section class="sheet letterhead" aria-label="Letterhead">
    <svg class="band" viewBox="0 0 420 56" width="420" height="56">
      <defs>
        <linearGradient id="lhBand" x1="0" y1="0" x2="1" y2="0">
          <stop offset="0" stop-color="var(--bright-blue)"/>
          <stop offset="0.5" stop-color="var(--navy)"/>
          <stop offset="1" stop-color="var(--bright-blue)"/>
        </linearGradient>
      </defs>
      <polygon points="0,0 420,0 420,26 230,26 205,50 0,50" fill="url(#lhBand)"/>
      <polyline points="0,50 205,50 230,26 420,26" fill="none" stroke="var(--sky)" stroke-width="1.5"/>
    </svg>
    <div class="brand"><span class="dot"></span><span>brightmendhome.example</span></div>
    <div class="tagline">caring from home everyday</div>
    <div class="watermark">brightmendhome.example</div>
    <div class="footer-block footer-contact">
      Phone 555 0142<br>hello@brightmendhome.example<br>Fax 555 0143<br>Mon–Fri 9–5
    </div>
    <div class="footer-block footer-address">
      brightmendhome.example<br>120 Harbor Lane, Suite 4<br>Springfield, ST 00000<br>United States
    </div>
  </section>

  <section class="sheet card" aria-label="Business card">
    <svg class="card-panel" viewBox="0 0 46 68" width="46" height="68">
      <defs>
        <linearGradient id="cardPanel" x1="0" y1="0" x2="1" y2="1">
          <stop offset="0" stop-color="var(--deep-blue)"/>
          <stop offset="1" stop-color="var(--navy)"/>
        </linearGradient>
      </defs>
      <polygon points="0,0 30,0 42,34 30,68 0,68" fill="url(#cardPanel)"/>
      <polyline points="30,0 42,34 30,68" fill="none" stroke="var(--sky)" stroke-width="1"/>
    </svg>
    <div class="brand"><span class="dot"></span><span>brightmendhome.example</span></div>
  </section>

  <section class="sheet envelope-front" aria-label="Envelope front">
    <svg class="band" viewBox="0 0 444 52" width="444" height="52">
      <defs>
        <linearGradient id="envBand" x1="0" y1="0" x2="1" y2="0">
          <stop offset="0" stop-color="var(--bright-blue)"/>
          <stop offset="0.45" stop-color="var(--navy)"/>
          <stop offset="1" stop-color="var(--bright-blue)"/>
        </linearGradient>
      </defs>
      <polygon points="0,0 444,0 444,48 260,48 222,28 184,48 0,48" fill="url(#envBand)"/>
      <polyline points="0,48 184,48 222,28 260,48 444,48" fill="none" stroke="var(--sky)" stroke-width="1.5"/>
    </svg>
  </section>

  <section class="sheet envelope-back" aria-label="Envelope back">
    <svg class="flap" viewBox="0 0 444 84" width="444" height="84">
      <defs>
        <linearGradient id="flapFill" x1="0" y1="0" x2="1" y2="0">
          <stop offset="0" stop-color="var(--bright-blue)"/>
          <stop offset="0.5" stop-color="var(--navy)"/>
          <stop offset="1" stop-color="var(--bright-blue)"/>
        </linearGradient>
      </defs>
      <path d="M0,0 H444 V8 Q436,12 430,24 L414,72 Q410,82 398,82 H46 Q34,82 30,72 L14,24 Q8,12 0,8 Z" fill="url(#flapFill)"/>
      <path d="M444,8 Q436,12 430,24 L414,72 Q410,82 398,82 H46 Q34,82 30,72 L14,24 Q8,12 0,8" fill="none" stroke="var(--sky)" stroke-width="1.5"/>
    </svg>
    <div class="brand"><span class="dot"></span><span>brightmend home</span></div>
  </section>

</main>
</body>
</html>
```